Consulting, Investors, Joint Venture Website

Founded in April 2018, Marendo Consultants Limited (MCL) is an advisory consulting firm specializing in engaging investors in business ventures in Tanzania.
With extensive experience in construction, energy, oil and gas and the legal professions, our team assembles our expertise that allows foreign investors to set foot and flourish in the Tanzanian market.
MCL is locally owned, founded and registered. Our shareholders are cultured Tanzanian citizens with extensive corporate experience in South Africa, Tanzania, United Kingdom and the United States.

Our mission is to provide responsive and unrivalled professional advice from learned and experienced professionals versed in the local market, with an understanding of the cultural and logistical challenges faced by foreign investors.

Our vision is to provide a complete investor’s package that initiates with company registration, compliance and documentation services and ultimately operational facilitation services.

Target Market(s)

Foreign Investors, International companies

Industry/Entity Type

Business Consultant

Number of Pages Required

5+ page

Requirements
Must have
• It will be 5 pages - Home, About Us, Services, Portfolio, Contact Us
Nice to have
• if it can look like https://www.plorvex.example/
• or https://www.dunetri.example or http://www.quillbrook.example/

```html
<!DOCTYPE html>
<html lang="en">
<head>
<meta charset="utf-8">
<title>Marendo Consultants</title>
<link href="https://fonts.googleapis.com/css2?family=Hind:wght@400;500;600;700&family=Catamaran:wght@500;600;700&display=swap" rel="stylesheet">
<style>
:root{
  --ink:#2e3039;
  --ink-soft:#3b3c44;
  --orange:#e39d5b;
  --orange-panel:rgba(222,150,88,.92);
  --slate-panel:#4a4c56;
  --blue-panel:#2f5580;
  --white:#ffffff;
  --muted:#8a8c94;
  --logo-blue:#1f63b5;
}
*{margin:0;padding:0;box-sizing:border-box}
html,body{width:1200px;height:717px;overflow:hidden;background:var(--white)}
body{font-family:"Hind",sans-serif;color:var(--ink);position:relative}

.topbar{position:absolute;left:0;top:0;width:1200px;height:31px;background:var(--ink);color:#c9cad0;font-size:10px;letter-spacing:.2px}
.topbar .address{position:absolute;left:232px;top:0;height:31px;display:flex;align-items:center;gap:10px}
.topbar .social{position:absolute;left:788px;top:12px;display:flex;gap:13px}
.topbar .social span{width:7px;height:7px;border-radius:50%;background:#8e9098;display:block}
.topbar .divider{position:absolute;left:884px;top:10px;width:1px;height:11px;background:#5a5c64}
.topbar .lang{position:absolute;left:905px;top:0;height:31px;display:flex;align-items:center;gap:4px;font-weight:600;color:var(--white);font-size:10px}
.topbar .menu{position:absolute;left:952px;top:10px;width:16px}
.topbar .menu i{display:block;height:2px;background:var(--white);margin-bottom:3px}

.header{position:absolute;left:0;top:31px;width:1200px;height:63px;background:var(--white)}
.brand{position:absolute;left:231px;top:18px;display:flex;align-items:center;gap:8px}
.brand .mark{width:22px;height:22px;background:var(--logo-blue)}
.brand .name{font-family:"Catamaran",sans-serif;font-weight:700;font-size:22px;color:var(--logo-blue);letter-spacing:1px;line-height:1}
.info{position:absolute;top:17px;display:flex;gap:10px;font-family:"Catamaran",sans-serif}
.info svg{margin-top:4px}
.info b{display:block;font-size:10px;font-weight:600;color:var(--ink);line-height:14px}
.info small{display:block;font-size:9px;font-weight:600;color:var(--muted);line-height:14px}

.hero{position:absolute;left:0;top:94px;width:1200px;height:453px;background:radial-gradient(ellipse at 60% 45%,#6a5848 0%,#54463b 45%,#3d332c 100%)}
.nav{position:absolute;left:231px;top:94px;width:539px;height:40px;background:var(--orange);display:flex;align-items:center;font-family:"Catamaran",sans-serif;font-size:13px;font-weight:600;color:var(--white)}
.nav a{color:inherit;text-decoration:none;margin-left:31px;margin-right:24px}
.nav a.active{color:var(--ink);margin-left:31px}
.callbar{position:absolute;left:770px;top:94px;width:430px;height:40px;background:var(--ink-soft);color:var(--orange);font-family:"Catamaran",sans-serif;font-weight:700;font-size:17px;padding-left:80px;line-height:42px;letter-spacing:.3px}

.hero-copy{position:absolute;left:232px;top:236px;color:var(--white)}
.hero-copy h1{font-weight:700;font-size:49px;line-height:45px;letter-spacing:-.5px}
.hero-copy p{margin-top:20px;width:380px;font-size:12.5px;line-height:16px}
.actions{position:absolute;left:232px;top:422px;display:flex;gap:13px}
.btn{width:108px;height:33px;display:flex;align-items:center;justify-content:center;font-size:12px;font-weight:600;color:var(--white)}
.btn.solid{background:var(--ink)}
.btn.ghost{border:1px solid var(--white)}
.arrow{position:absolute;top:298px;width:44px;height:44px;border-radius:50%;background:rgba(70,62,55,.7);display:flex;align-items:center;justify-content:center}

.features{position:absolute;left:0;top:547px;width:1200px;height:170px;display:flex}
.feature{width:400px;height:170px;position:relative;color:var(--white)}
.feature.orange{background:var(--orange-panel)}
.feature.slate{background:var(--slate-panel)}
.feature.blue{background:var(--blue-panel)}
.feature .icon{position:absolute;left:44px;top:36px}
.feature h2{position:absolute;left:101px;top:40px;font-weight:500;font-size:25px;line-height:28px}
.feature p{position:absolute;left:101px;top:77px;width:260px;font-size:12px;line-height:15.5px}
</style>
</head>
<body>

<div class="topbar">
  <div class="address">
    <svg width="12" height="14" viewBox="0 0 12 14"><path d="M6 13S1 8 1 5a5 5 0 0 1 10 0c0 3-5 8-5 8z" fill="none" stroke="#c9cad0"/><circle cx="6" cy="5" r="1.7" fill="none" stroke="#c9cad0"/></svg>
    118, BAOBAB LANE, HARBOUR SQUARE, TANZANIA, 4521
  </div>
  <div class="social"><span></span><span></span><span></span><span></span></div>
  <div class="divider"></div>
  <div class="lang">EN <svg width="8" height="5"><path d="M0 0h8L4 5z" fill="#fff"/></svg></div>
  <div class="menu"><i></i><i></i><i></i></div>
</div>

<div class="header">
  <div class="brand"><span class="mark"></span><span class="name">MARENDO</span></div>
  <div class="info" style="left:536px">
    <svg width="14" height="18" viewBox="0 0 14 18"><path d="M7 17S1 10.5 1 6.5a6 6 0 0 1 12 0C13 10.5 7 17 7 17z" fill="none" stroke="#e39d5b" stroke-width="1.2"/><circle cx="7" cy="6.5" r="2" fill="none" stroke="#e39d5b" stroke-width="1.2"/></svg>
    <div><b>2740 Orchard Crest Road</b><small>Lakeview, TX 70911</small></div>
  </div>
  <div class="info" style="left:706px">
    <svg width="17" height="17" viewBox="0 0 17 17"><path d="M3 1l3 3-2 2c1 3 3 5 6 6l2-2 3 3-2 3C7 16 1 10 1 3z" fill="none" stroke="#e39d5b" stroke-width="1.2"/></svg>
    <div><b>+(1800) 555 014</b><small>Toll Free</small></div>
  </div>
  <div class="info" style="left:841px">
    <svg width="17" height="18" viewBox="0 0 17 18"><circle cx="8.5" cy="10" r="7" fill="none" stroke="#e39d5b" stroke-width="1.2"/><path d="M8.5 6v4l3 2M6 1h5" fill="none" stroke="#e39d5b" stroke-width="1.2"/></svg>
    <div><b>Mon - Sat 9.00 - 19.00</b><small>Sunday CLOSED</small></div>
  </div>
</div>

<section class="hero" role="img" aria-label="Photo of colleagues bumping fists over a desk with laptops and notebooks"></section>

<nav class="nav">
  <a class="active">Home</a><a>About Us</a><a>Services</a><a>Portfolio</a><a>Contact Us</a>
</nav>
<div class="callbar">1800.555.014.</div>

<div class="arrow" style="left:3px"><svg width="12" height="18"><path d="M10 1L2 9l8 8" fill="none" stroke="#fff" stroke-width="1.6"/></svg></div>
<div class="arrow" style="left:1153px"><svg width="12" height="18"><path d="M2 1l8 8-8 8" fill="none" stroke="#fff" stroke-width="1.6"/></svg></div>

<div class="hero-copy">
  <h1>We help in<br>grow your business</h1>
  <p>We counsel on speculations, make marketable strategies starting with no outside help, aid vital arranging, administration, property administration and numerous different issues.</p>
</div>
<div class="actions">
  <div class="btn solid">Our services</div>
  <div class="btn ghost">Read more</div>
</div>

<section class="features">
  <div class="feature orange" role="img" aria-label="Orange-tinted photo of a workspace behind the panel">
    <svg class="icon" width="44" height="44" viewBox="0 0 44 44"><circle cx="22" cy="22" r="21" fill="none" stroke="#fff" stroke-width="1.5"/><circle cx="22" cy="17" r="7" fill="none" stroke="#fff" stroke-width="1.5"/><path d="M9 35c3-7 8-9 13-9s10 2 13 9" fill="none" stroke="#fff" stroke-width="1.5"/></svg>
    <h2>Expert Advisors</h2>
    <p>Lorem ipsum dolor sit amet, consectetur adipisicing elit, sed do eiusmod tempor incididunt ut labore et dolore magna aliqua</p>
  </div>
  <div class="feature slate" role="img" aria-label="Dark-tinted photo of a business meeting behind the panel">
    <svg class="icon" width="44" height="44" viewBox="0 0 44 44"><circle cx="22" cy="22" r="21" fill="none" stroke="#fff" stroke-width="1.5"/><path d="M10 22h23M25 14l8 8-8 8" fill="none" stroke="#fff" stroke-width="1.5"/></svg>
    <h2>Business Consultants</h2>
    <p>Lorem ipsum dolor sit amet, consectetur adipisicing elit, sed do eiusmod tempor incididunt ut labore et dolore magna aliqua</p>
  </div>
  <div class="feature blue" role="img" aria-label="Blue-tinted photo of a person working at a laptop behind the panel">
    <svg class="icon" width="44" height="44" viewBox="0 0 44 44"><circle cx="22" cy="22" r="21" fill="none" stroke="#fff" stroke-width="1.5"/><circle cx="27" cy="12" r="3.5" fill="none" stroke="#fff" stroke-width="1.5"/><circle cx="14" cy="23" r="3.5" fill="none" stroke="#fff" stroke-width="1.5"/><circle cx="24" cy="33" r="3.5" fill="none" stroke="#fff" stroke-width="1.5"/><path d="M24.5 14.5l-8 6M16.5 25.5l5 5" fill="none" stroke="#fff" stroke-width="1.5"/></svg>
    <h2>Facilitation Services</h2>
    <p>Lorem ipsum dolor sit amet, consectetur adipisicing elit, sed do eiusmod tempor incididunt ut labore et dolore magna aliqua</p>
  </div>
</section>

</body>
</html>
```